Professional, Attractive, Simple Website Needed!!

We completed the design for our logo.

We need a website built out around this.

Here are a couple samples of how we want ours formatted.

http://brvntapower.com

http://www.halvorbeam.com/lp/free-quote?LeadSource=Search%20Engine&ProgramName=webquery&experience=qual&language=en&type=brd&gclid=Xq7RTPwmEYKDLAvUHbsNQkfPZrTcGwnJuoVbXeLqHmRYdAsWtPkMcNfBYgzTrUoQJhEdWvKpYaLsZbCmNDgQwTxAoKpXbT_qkR

http://morvalo.co

Reason: Extending this deadline due to our delay in providing designers with content for each page. This is coming in next 24 hours.

Reason: Due to scheduling conflicts and extended travel delays related to Puerto Rico, the deadline has been extended. Your patience is greatly appreciated.

Reason: Travel and scheduling conflicts have made it impossible to give this project the thorough review it deserves, therefore I am extending the deadline. Thank you for your patience!

Target Market(s)

Home Owners who earn 60k + household annually

Industry/Entity Type

It Professional

Coding

Coded - Design and coding required

Number of Pages Required

5+ page

Font styles to use
Serif

Colors
34a7d8
9bcb3c

Requirements
Must have
• Simple
• Lead form Entry (Ability for visitor to enter Name, number and address for a quote)
• Sleek Design
• Professional
• Testimonials
• Use color Scheme of Design Logo Attached
Nice to have
• Video when site starts
• Like this
• https://www.vidmarrow.com/watch?v=qT8mRpXw2Ka&feature=vidm.ro
Should not have
• Should not include Commercial solar
• Should not include wind power

```html
<!DOCTYPE html>
<html lang="en">
<head>
<meta charset="utf-8">
<title>Bright Field Energy</title>
<link href="https://fonts.googleapis.com/css2?family=Raleway:wght@400;500;600;700&display=swap" rel="stylesheet">
<style>
:root{
  --blue:#34a7d8;
  --green:#9bcb3c;
  --ink:#2b2b2b;
  --text:#555;
  --line:#e3e3e3;
  --white:#fff;
}
*{box-sizing:border-box;margin:0;padding:0}
html,body{width:1200px;height:2980px;overflow:hidden;background:var(--white)}
body{font-family:'Raleway',sans-serif;color:var(--text)}
.page{position:relative;width:1200px;height:2980px;overflow:hidden;background:var(--white)}
.abs{position:absolute}

/* hero */
.hero-photo{position:absolute;left:0;top:0;width:1200px;height:660px;
  background:linear-gradient(180deg,#0d1d33 0%,#1d4f86 28%,#3a6fa6 45%,#b9532a 62%,#c8693a 72%,#4e7d2c 88%,#3f6e25 100%);
  clip-path:polygon(0 0,1200px 0,1200px 600px,780px 560px,0 640px)}
.hero-edge{position:absolute;left:0;top:540px}
.brand{position:absolute;left:100px;top:60px;display:flex;align-items:center;gap:10px;color:var(--white);font-weight:700;font-size:22px;letter-spacing:.5px}
.brand-dot{width:22px;height:22px;border-radius:50%;background:var(--green)}
.nav{position:absolute;left:400px;top:86px;display:flex;font-size:13px;font-weight:500;color:var(--white)}
.nav a{color:var(--white);text-decoration:none;text-transform:uppercase;margin-right:40px;padding-bottom:10px}
.nav a.active{border-bottom:2px solid var(--green)}
.login{position:absolute;left:1000px;top:78px;width:100px;height:34px;background:var(--green);color:var(--white);font-size:13px;font-weight:600;display:flex;align-items:center;justify-content:center;gap:6px;border-radius:2px}
.hero-ring{position:absolute;left:550px;top:196px;width:100px;height:100px;border:5px solid rgba(255,255,255,.9);border-radius:50%}
.hero-title{position:absolute;left:0;width:1200px;top:324px;text-align:center;color:var(--white);font-size:48px;font-weight:700;letter-spacing:1px}
.play{position:absolute;left:580px;top:408px;width:40px;height:40px;border-radius:50%;border:2px solid var(--white);display:flex;align-items:center;justify-content:center}

/* lead form */
.lead{position:absolute;left:420px;top:490px;width:370px;height:310px;background:#f0f0f0;border:1px solid #ddd;box-shadow:0 2px 10px rgba(0,0,0,.12);text-align:center}
.lead h2{font-size:23px;font-weight:500;color:var(--ink);margin-top:28px;letter-spacing:.5px}
.lead .field{display:block;margin:10px auto 0;width:310px;height:32px;background:var(--white);border:1px solid #e6e6e6;font-size:11px;color:#999;text-align:left;padding:9px 14px}
.lead .field:first-of-type{margin-top:20px}
.lead .go{display:block;margin:18px auto 0;width:310px;height:36px;background:var(--blue);color:var(--white);font-size:13px;font-weight:700;letter-spacing:2px;line-height:36px}
.lead .note{margin-top:14px;font-size:11px;color:#777;text-decoration:underline;font-style:italic}

/* steps */
.steps{position:absolute;left:0;top:800px;width:1200px;height:456px;background:linear-gradient(180deg,#fff 0%,#f7f7f8 100%)}
.sec-title{position:absolute;left:0;width:1200px;text-align:center;font-size:28px;font-weight:500;letter-spacing:3px;color:var(--ink);text-transform:uppercase}
.sec-rule{position:absolute;left:540px;width:120px;height:3px;background:var(--green)}
.step-label{position:absolute;width:200px;text-align:center;font-size:14px;line-height:22px;color:#444}

/* news */
.news{position:absolute;left:0;top:1256px;width:1200px;height:604px;background:linear-gradient(180deg,#8dc63f 0%,#94c845 60%,#86bd3a 100%)}
.news .sec-title{color:var(--white)}
.news .sec-rule{background:var(--white)}
.card{position:absolute;top:168px;width:316px;height:356px;background:var(--white);box-shadow:0 3px 10px rgba(0,0,0,.15)}
.card-img{position:absolute;left:0;top:0;width:316px;height:206px;clip-path:polygon(0 0,100% 0,100% 170px,50% 206px,0 170px)}
.card-chev{position:absolute;left:0;top:166px}
.card h3{position:absolute;top:232px;left:0;width:316px;text-align:center;font-size:14px;font-weight:600;color:#333;text-transform:uppercase}
.card p{position:absolute;top:258px;left:20px;width:276px;text-align:center;font-size:12px;line-height:27px;color:#666}

/* testimonials */
.testis{position:absolute;left:0;top:1860px;width:1200px;height:720px;background:#f2f2f3}
.avatar{position:absolute;width:152px;height:152px;border-radius:50%;border:5px solid var(--white);box-shadow:0 2px 8px rgba(0,0,0,.2)}
.quote{position:absolute;background:var(--white);box-shadow:0 2px 8px rgba(0,0,0,.1);padding:26px 36px;font-size:12px;line-height:30px;color:#666}
.quote .who{margin-top:4px;font-size:13px;color:#333;font-weight:500}
.quote .role{color:var(--blue);font-size:12px;margin-left:6px}
.quote .stars{color:#f2c200;font-size:11px;margin-left:6px;letter-spacing:1px}
.dots{position:absolute;left:578px;top:2412px;display:flex;gap:8px}
.dots span{width:8px;height:8px;border-radius:50%;border:1px solid var(--blue)}
.dots span.on{background:var(--blue)}

/* footer */
.foot-edge{position:absolute;left:0;top:2470px}
.foot-brand{position:absolute;left:100px;top:2690px;display:flex;align-items:center;gap:10px;font-size:24px;font-weight:700;color:var(--blue)}
.foot-brand .dot{width:26px;height:26px;border-radius:50%;background:var(--green)}
.foot-col h4{font-size:15px;font-weight:600;color:#333;text-transform:uppercase;letter-spacing:.5px}
.contact{position:absolute;left:364px;top:2636px;width:240px}
.contact .row{display:flex;gap:14px;font-size:12px;line-height:22px;color:#666;margin-top:14px}
.contact svg{flex:none;margin-top:3px}
.socials{display:flex;gap:10px;margin-top:18px}
.socials span{width:32px;height:32px;border-radius:3px}
.links{position:absolute;left:650px;top:2636px}
.links li{list-style:none;font-size:13px;color:#555;margin-top:20px}
.links li::before{content:"»";color:var(--blue);margin-right:18px}
.links ul{margin-top:2px}
.subscribe{position:absolute;left:810px;top:2636px;width:296px}
.subscribe p{font-size:11px;line-height:20px;color:#777;margin-top:14px}
.subscribe .field{margin-top:10px;height:42px;border:1px solid #ddd;font-size:11px;color:#777;padding:14px 12px}
.subscribe .btn{margin-top:14px;width:100px;height:42px;background:var(--green);color:var(--white);font-size:12px;font-weight:600;text-align:center;line-height:42px;text-transform:uppercase}
.foot-rule{position:absolute;left:100px;top:2912px;width:1006px;height:1px;background:var(--line)}
.copy{position:absolute;left:0;width:1200px;top:2948px;text-align:center;font-size:12px;color:#666}
</style>
</head>
<body>
<div class="page">

  <!-- hero -->
  <div class="hero-photo" role="img" aria-label="House with orange tiled roof covered in solar panels under a dark blue sky"></div>
  <svg class="hero-edge" width="1200" height="140" viewBox="0 540 1200 140" aria-hidden="true">
    <polygon points="0,640 780,560 1200,600 1200,618 780,578 0,658" fill="#9bcb3c"/>
    <polygon points="780,578 1200,618 1200,664 600,600" fill="#34a7d8"/>
    <polygon points="0,658 780,578 600,600 1200,664 1200,680 0,680" fill="#ffffff"/>
  </svg>

  <div class="brand"><span class="brand-dot"></span>Bright Field Energy</div>
  <nav class="nav">
    <a class="active">Home</a><a>About Us</a><a>Services</a><a>How it works</a><a>Blog</a><a>Contact Us</a>
  </nav>
  <div class="login">
    <svg width="10" height="12" viewBox="0 0 10 12"><rect x="0" y="5" width="10" height="7" rx="1" fill="#fff"/><path d="M2 5V3.5a3 3 0 0 1 6 0V5" stroke="#fff" stroke-width="1.5" fill="none"/></svg>
    LOG IN
  </div>

  <div class="hero-ring"></div>
  <h1 class="hero-title">BRIGHT FIELD ENERGY</h1>
  <div class="play"><svg width="14" height="16" viewBox="0 0 14 16"><polygon points="2,1 13,8 2,15" fill="#fff"/></svg></div>

  <form class="lead">
    <h2>START SAVING TODAY</h2>
    <div class="field">Enter Name *</div>
    <div class="field">Phone Number *</div>
    <div class="field">Address *</div>
    <div class="go">GET STARTED</div>
    <div class="note">* Fields as Required</div>
  </form>

  <!-- steps -->
  <section class="steps">
    <h2 class="sec-title" style="top:66px">4 Easy Steps to Going Solar</h2>
    <div class="sec-rule" style="top:118px"></div>
    <svg class="abs" style="left:0;top:0" width="1200" height="456" viewBox="0 800 1200 456" aria-hidden="true">
      <g fill="none" stroke-width="3" stroke-dasharray="2 5" stroke-linecap="round">
        <line x1="197" y1="1060" x2="284" y2="1060" stroke="#34a7d8"/>
        <path d="M385 1026 Q448 950 511 1026" stroke="#9bcb3c"/>
        <path d="M385 1094 Q448 1130 511 1094" stroke="#34a7d8"/>
        <path d="M601 1026 Q664 950 727 1026" stroke="#34a7d8"/>
        <path d="M601 1094 Q664 1130 727 1094" stroke="#9bcb3c"/>
        <path d="M817 1026 Q880 950 943 1026" stroke="#9bcb3c"/>
        <path d="M817 1094 Q880 1130 943 1094" stroke="#34a7d8"/>
      </g>
      <g>
        <circle cx="340" cy="1060" r="56" fill="#e9e9ea"/><circle cx="340" cy="1060" r="45" fill="#34a7d8"/>
        <circle cx="556" cy="1060" r="56" fill="#e9e9ea"/><circle cx="556" cy="1060" r="45" fill="#34a7d8"/>
        <circle cx="772" cy="1060" r="56" fill="#e9e9ea"/><circle cx="772" cy="1060" r="45" fill="#34a7d8"/>
        <circle cx="988" cy="1060" r="56" fill="#e9e9ea"/><circle cx="988" cy="1060" r="45" fill="#34a7d8"/>
      </g>
      <!-- headset -->
      <path d="M322 1070 v-10 a18 18 0 0 1 36 0 v10" fill="none" stroke="#fff" stroke-width="4"/>
      <rect x="318" y="1060" width="9" height="17" rx="3" fill="#fff"/>
      <rect x="353" y="1060" width="9" height="17" rx="3" fill="#fff"/>
      <!-- panel -->
      <polygon points="534,1072 543,1050 579,1050 570,1072" fill="#fff"/>
      <g stroke="#34a7d8" stroke-width="2">
        <line x1="552" y1="1050" x2="544" y2="1072"/><line x1="561" y1="1050" x2="553" y2="1072"/><line x1="570" y1="1050" x2="562" y2="1072"/>
        <line x1="538" y1="1061" x2="575" y2="1061"/>
      </g>
      <!-- calendar -->
      <rect x="754" y="1043" width="36" height="34" rx="3" fill="none" stroke="#fff" stroke-width="3"/>
      <rect x="754" y="1043" width="36" height="8" fill="#fff"/>
      <g fill="#fff">
        <rect x="759" y="1056" width="6" height="5"/><rect x="769" y="1056" width="6" height="5"/><rect x="779" y="1056" width="6" height="5"/>
        <rect x="759" y="1066" width="6" height="5"/><rect x="769" y="1066" width="6" height="5"/><rect x="779" y="1066" width="6" height="5"/>
      </g>
      <text x="988" y="1073" text-anchor="middle" font-family="Raleway,sans-serif" font-size="36" font-weight="600" fill="#fff">$</text>
      <g font-family="Raleway,sans-serif" font-size="14" font-weight="700" fill="#fff" text-anchor="middle">
        <circle cx="180" cy="1060" r="18" fill="#9bcb3c"/><text x="180" y="1065">1</text>
        <circle cx="448" cy="990" r="18" fill="#9bcb3c"/><text x="448" y="995">2</text>
        <circle cx="664" cy="1112" r="18" fill="#9bcb3c"/><text x="664" y="1117">3</text>
        <circle cx="880" cy="990" r="18" fill="#9bcb3c"/><text x="880" y="995">4</text>
      </g>
    </svg>
    <div class="step-label" style="left:240px;top:336px">Speak to a<br>solar consultant</div>
    <div class="step-label" style="left:456px;top:336px">We'll design your<br>solar panel system</div>
    <div class="step-label" style="left:672px;top:336px">Schedule your<br>1 day install</div>
    <div class="step-label" style="left:888px;top:336px">Start saving on your<br>electricity bill</div>
  </section>

  <!-- news -->
  <section class="news">
    <h2 class="sec-title" style="top:74px">Recent News</h2>
    <div class="sec-rule" style="top:128px"></div>

    <article class="card" style="left:100px">
      <div class="card-img" role="img" aria-label="Installers fitting solar panels on a roof" style="background:linear-gradient(160deg,#7fb3e2 0%,#3f78b8 55%,#23426e 100%)"></div>
      <svg class="card-chev" width="316" height="44" viewBox="0 0 316 44" aria-hidden="true"><polyline points="0,4 158,40 316,4" fill="none" stroke="#9bcb3c" stroke-width="3"/></svg>
      <h3>Sed ut perspiciatis unde omni</h3>
      <p>Nemo enim ipsam voluptatem quia voluptas sit aspernatur aut odit aut fugit sed quia consequuntur mat aut fugit sed qugni dolores.</p>
    </article>

    <article class="card" style="left:446px">
      <div class="card-img" role="img" aria-label="Rows of solar panels on a flat rooftop" style="background:linear-gradient(170deg,#c9d6e2 0%,#8a9bb0 45%,#34507a 100%)"></div>
      <svg class="card-chev" width="316" height="44" viewBox="0 0 316 44" aria-hidden="true"><polyline points="0,4 158,40 316,4" fill="none" stroke="#9bcb3c" stroke-width="3"/></svg>
      <h3>Architecto beatae vitae dicta</h3>
      <p>Nemo enim ipsam voluptatem quia voluptas sit aspernatur aut odit aut fugit sed quia consequuntur mat aut fugit sed qugni dolores.</p>
    </article>

    <article class="card" style="left:794px">
      <div class="card-img" role="img" aria-label="Solar panels at sunset with a glowing sky" style="background:linear-gradient(180deg,#4b3a7a 0%,#c46a6a 40%,#f2b04a 58%,#2e3f6e 100%)"></div>
      <svg class="card-chev" width="316" height="44" viewBox="0 0 316 44" aria-hidden="true"><polyline points="0,4 158,40 316,4" fill="none" stroke="#9bcb3c" stroke-width="3"/></svg>
      <h3>Aliquip ex ea commodonsequa</h3>
      <p>Nemo enim ipsam voluptatem quia voluptas sit aspernatur aut odit aut fugit sed quia consequuntur mat aut fugit sed qugni dolores.</p>
    </article>
  </section>

  <!-- testimonials -->
  <section class="testis">
    <h2 class="sec-title" style="top:64px">Testimonials</h2>
    <div class="sec-rule" style="top:118px"></div>
  </section>
  <div class="avatar" role="img" aria-label="Portrait of a smiling male customer" style="left:120px;top:2024px;background:linear-gradient(180deg,#cfe2f0 0%,#d9b9a0 45%,#2d4a80 100%)"></div>
  <div class="quote" style="left:324px;top:2026px;width:768px;height:154px">
    " Sed ut perspiciatis unde omnis iste natus error sit voluptatem accusantium doloremque laudantium, totam rem aperiam, eaque ipsa quae ab illo inventore veritatis et quasi architecto beatae vitae dicta sunt explicabo "
    <div class="who">QUIS NOSTRUD EXE <span class="role">quasi architecto</span><span class="stars">★★★★★</span></div>
  </div>
  <div class="quote" style="left:116px;top:2216px;width:770px;height:160px">
    " Lorem ipsum dolor sit amet, consectetur adipiscing elit, sed do eiusmod tempor incididunt ut labore et dolore magna aliqua. Ut enim ad minim veniam, quis nostrud exercitation ullamco laboris nisicommodo consequat "
    <div class="who">QUIS NOSTRUD EXE <span class="role">quasi architecto</span><span class="stars">★★★★★</span></div>
  </div>
  <div class="avatar" role="img" aria-label="Portrait of a smiling female customer" style="left:932px;top:2218px;background:linear-gradient(180deg,#a35a3e 0%,#d9b39a 50%,#6a3f2e 100%)"></div>
  <div class="dots"><span class="on"></span><span></span><span></span></div>

  <!-- footer -->
  <svg class="foot-edge" width="1200" height="140" viewBox="0 2470 1200 140" aria-hidden="true">
    <polygon points="0,2560 600,2470 1200,2560 1200,2610 0,2610" fill="#ffffff"/>
    <polygon points="0,2560 600,2470 1200,2560 1200,2574 600,2484 0,2574" fill="#9bcb3c"/>
    <polygon points="0,2574 600,2484 1200,2574 1200,2586 600,2498 0,2596" fill="#34a7d8"/>
    <polygon points="0,2596 600,2498 1200,2586 1200,2610 0,2610" fill="#ffffff"/>
    <circle cx="600" cy="2560" r="30" fill="none" stroke="#eef0f1" stroke-width="4"/>
  </svg>

  <div class="foot-brand"><span class="dot"></span>Bright Field Energy</div>

  <div class="contact foot-col">
    <h4>Get in Touch</h4>
    <div class="row" style="margin-top:22px">
      <svg width="14" height="18" viewBox="0 0 14 18"><path d="M7 1a6 6 0 0 1 6 6c0 4-6 10-6 10S1 11 1 7a6 6 0 0 1 6-6z" fill="none" stroke="#34a7d8" stroke-width="1.5"/><circle cx="7" cy="7" r="2" fill="none" stroke="#34a7d8" stroke-width="1.5"/></svg>
      <span>54,voluptate velit esse cillueu<br>fugiat nulla pariatu.</span>
    </div>
    <div class="row">
      <svg width="14" height="16" viewBox="0 0 14 16"><path d="M3 1l3 3-2 2c1 2 3 4 5 5l2-2 3 3-2 2C6 14 1 8 1 3z" fill="none" stroke="#34a7d8" stroke-width="1.4"/></svg>
      <span>Phone : (555) - 014 - 2238</span>
    </div>
    <div class="row">
      <svg width="16" height="12" viewBox="0 0 16 12"><rect x="1" y="1" width="14" height="10" fill="none" stroke="#34a7d8" stroke-width="1.4"/><polyline points="1,1 8,7 15,1" fill="none" stroke="#34a7d8" stroke-width="1.4"/></svg>
      <span>info@brightfield.example</span>
    </div>
    <div class="socials">
      <span style="background:#3b5a98"></span><span style="background:#2ba9e1"></span><span style="background:#f0822f"></span><span style="background:#d64a36"></span>
    </div>
  </div>

  <div class="links foot-col">
    <h4>Quick Links</h4>
    <ul><li>Home</li><li>About Us</li><li>Services</li><li>How it works</li><li>Contact Us</li></ul>
  </div>

  <div class="subscribe foot-col">
    <h4>Subscribe to Newsletter</h4>
    <p>Excepteur sint occaecat cupidatat non proident, sunt in culpa qui Nemo enim ipsam voluptatem</p>
    <div class="field">Enter Name</div>
    <div class="btn">Subscribe</div>
  </div>

  <div class="foot-rule"></div>
  <div class="copy">Copyright © Bright Field Energy 2017. All rights reserved &nbsp;|&nbsp; Privacy policy</div>
</div>
</body>
</html>
```